Brindle cards

I am in the auto motive, transportation business I would like a business card that is Something cool, modern edgy, having to do with car culture. I offer towing service for high and exotic cars. I also provide towing for collisions and car accidents. I offer open and enclosed transport nationwide.

Target Market(s)

Car culture people high end auto collectors

Industry/Entity Type

Towing car carrier

Contact Information for Business Card

My company colors black yellow and silver

Font styles to use
Serif

```html
<!DOCTYPE html>
<html lang="en">
<head>
<meta charset="utf-8">
<title>Brindle Business Card</title>
<link href="https://fonts.googleapis.com/css2?family=Roboto+Slab:wght@400;700&display=swap" rel="stylesheet">
<style>
  :root {
    --page-bg: #ececec;
    --card-bg: #2e2e2e;
    --card-edge: #e8cf3a;
    --accent: #f1d233;
    --text-light: #f2f2f2;
    --rule: #d9d9d9;
    --emboss-dark: #151515;
    --emboss-mid: #424242;
  }
  * { margin: 0; padding: 0; box-sizing: border-box; }
  html, body { width: 1200px; height: 802px; overflow: hidden; }
  body {
    background: var(--page-bg);
    font-family: "Roboto Slab", Georgia, serif;
    display: flex;
    align-items: center;
    justify-content: center;
    gap: 40px;
  }
  .card {
    position: relative;
    width: 540px;
    height: 309px;
    background: var(--card-bg);
    border: 3px solid var(--card-edge);
    overflow: hidden;
  }
  /* Front */
  .brand {
    position: absolute;
    top: 50px;
    right: 48px;
    display: flex;
    align-items: center;
    gap: 10px;
  }
  .brand-dot {
    width: 18px; height: 18px;
    border-radius: 50%;
    background: var(--accent);
  }
  .brand-name {
    font-weight: 700;
    font-size: 42px;
    line-height: 1;
    color: var(--text-light);
    text-transform: uppercase;
    letter-spacing: 1px;
  }
  .person {
    position: absolute;
    left: 36px;
    top: 126px;
  }
  .person-name {
    font-weight: 700;
    font-size: 20px;
    color: var(--accent);
    text-transform: uppercase;
    line-height: 1.1;
  }
  .person-role {
    font-size: 14px;
    line-height: 1.2;
    color: var(--text-light);
    margin-top: 3px;
  }
  .divider {
    position: absolute;
    left: 36px; right: 36px;
    top: 178px;
    height: 1px;
    background: var(--rule);
  }
  .contacts {
    position: absolute;
    left: 56px;
    top: 196px;
    list-style: none;
  }
  .contacts li {
    display: flex;
    align-items: center;
    gap: 10px;
    font-size: 14px;
    color: var(--text-light);
    line-height: 1;
    margin-bottom: 12px;
  }
  .contacts svg { width: 13px; height: 13px; flex: none; }
  .address {
    position: absolute;
    right: 40px;
    top: 196px;
    text-align: right;
    font-size: 14px;
    line-height: 1.45;
    color: var(--text-light);
  }
  /* Back */
  .back-brand {
    position: absolute;
    left: 26px;
    top: 124px;
    font-weight: 700;
    font-size: 36px;
    line-height: 1;
    color: var(--emboss-mid);
    text-transform: uppercase;
  }
  .truck-art {
    position: absolute;
    left: 250px;
    top: 60px;
    width: 270px;
    height: 230px;
    border-radius: 8px;
    background: linear-gradient(160deg, var(--emboss-mid) 0%, var(--emboss-dark) 70%);
    opacity: 0.85;
  }
</style>
</head>
<body>
  <section class="card card-front">
    <div class="brand">
      <span class="brand-dot"></span>
      <span class="brand-name">Brindle</span>
    </div>
    <div class="person">
      <p class="person-name">Marcus Hale</p>
      <p class="person-role">Manager</p>
    </div>
    <div class="divider"></div>
    <ul class="contacts">
      <li>
        <svg viewBox="0 0 14 14"><circle cx="7" cy="7" r="7" fill="var(--accent)"/><path d="M4.5 3.5l1.5 1.5-1 1c.6 1.3 1.7 2.4 3 3l1-1 1.5 1.5-1.2 1.2C6.5 10.3 3.7 7.5 3.3 4.7z" fill="var(--card-bg)"/></svg>
        555-014-2100
      </li>
      <li>
        <svg viewBox="0 0 14 14"><rect x="1" y="3" width="12" height="8" fill="var(--accent)"/><path d="M1 3l6 5 6-5" stroke="var(--card-bg)" stroke-width="1.2" fill="none"/></svg>
        hello@brindletow.com
      </li>
      <li>
        <svg viewBox="0 0 14 14"><circle cx="7" cy="7" r="6.5" fill="var(--accent)"/><circle cx="7" cy="7" r="2.5" fill="var(--card-bg)"/></svg>
        www.brindletow.com
      </li>
    </ul>
    <p class="address">Your Address, City<br>State, Zip 0000</p>
  </section>

  <section class="card card-back">
    <span class="back-brand">Brindle</span>
    <div class="truck-art" role="img" aria-label="Large embossed silhouette of a flatbed tow truck"></div>
  </section>
</body>
</html>
```